Cafe Menu Design

Design a menu for a cafe with the following description:
1- cafe name: fizzle finch
2- logo: Giddy wren (logo attached)
products:
1- bubble tea (juices + tea) - google the concept
2- waffles (special honeycomb shape waffles)
3- juices
4- coffee

Colors

Designer to choose colors to be used in the design.

Requirements
Must have
• must have description of the bubble tea and how to order on one side.
Nice to have
• items pics must be there: (there is a white transparent cup with colored bubbles. we can change color of the white if possible to match the fruit color in the menu)

```html
<!DOCTYPE html>
<html lang="en">
<head>
<meta charset="utf-8">
<title>fizzle finch — Milk Tea Menu</title>
<link rel="stylesheet" href="https://fonts.googleapis.com/css2?family=Exo+2:wght@400;700&family=Fredoka:wght@700&display=swap">
<style>
  :root {
    --paper: #f4f3f0;
    --paper-edge: #dcdad5;
    --panel: rgba(243, 206, 110, 0.78);
    --ink: #111111;
    --gold: #c79a1e;
    --band: #f2c431;
    --cup: #d9a27a;
    --mango: #f0a23a;
    --berry: #d8323a;
    --rasp: #d42d55;
  }
  * { margin: 0; padding: 0; box-sizing: border-box; }
  html, body { width: 849px; height: 1200px; overflow: hidden; }
  body { background: var(--paper); font-family: "Exo 2", sans-serif; color: var(--ink); }
  .menu { position: relative; width: 849px; height: 1200px; overflow: hidden;
    background: linear-gradient(180deg, var(--paper-edge), var(--paper) 30%); }
  .stage { position: absolute; left: 0; top: 0; }
  .pattern-band { position: absolute; left: 0; top: 0; width: 849px; height: 150px;
    background: linear-gradient(180deg, #d6d4cf, #e9e8e4); }
  .photo { position: absolute; }
  .photo-cup { left: 0; top: 216px; width: 216px; height: 504px; border-radius: 0 14px 14px 0;
    background: linear-gradient(180deg, #c98c62, var(--cup) 40%, #ebc7ab); }
  .photo-mango { left: 696px; top: 296px; width: 153px; height: 456px; border-radius: 120px 0 0 120px;
    background: linear-gradient(135deg, #e2463a, var(--mango) 55%, #f7d23a); }
  .photo-strawberries { left: 0; top: 936px; width: 296px; height: 216px; border-radius: 0 120px 0 0;
    background: radial-gradient(circle at 40% 60%, #e8504a, var(--berry) 60%, #a81f25); }
  .photo-raspberries { left: 664px; top: 928px; width: 185px; height: 216px; border-radius: 100px 0 0 0;
    background: radial-gradient(circle at 60% 60%, #e84a70, var(--rasp) 60%, #5e9a3a); }
  .mascot-small { position: absolute; left: 13px; top: 770px; width: 56px; height: 56px; border-radius: 50%;
    background: linear-gradient(180deg, #ffffff, var(--band)); }
  .band-bottom { position: absolute; left: 0; bottom: 0; width: 849px; height: 48px; background: var(--band); }

  .title { position: absolute; left: 0; width: 849px; text-align: center;
    font-family: "Fredoka", sans-serif; font-weight: 700; line-height: 1; }
  .title-main { top: 110px; font-size: 42px; }
  .title-specials { top: 862px; left: 220px; width: 436px; font-size: 44px; }
  .subline { position: absolute; left: 0; width: 849px; text-align: center; font-size: 21px; line-height: 1; }

  .panel { position: absolute; background: var(--panel); border-radius: 18px; text-align: center; }
  .panel h2 { font-weight: 700; font-size: 26px; letter-spacing: 0.5px; line-height: 1; padding-top: 12px; }
  .panel p { font-size: 21px; line-height: 1; margin-top: 8px; }
  .panel-base { left: 228px; top: 192px; width: 418px; height: 70px; }
  .panel-sugar { left: 228px; top: 276px; width: 418px; height: 70px; }
  .panel-flavor { left: 228px; top: 360px; width: 418px; height: 187px; }
  .panel-toppings { left: 192px; top: 560px; width: 490px; height: 274px; }

  .list { position: absolute; list-style: none; font-size: 21px; line-height: 29.2px; text-align: left; }
  .flavor-a { left: 73px; top: 39px; }
  .flavor-b { left: 218px; top: 39px; }
  .topping-a { left: 8px; top: 38px; }
  .topping-b { left: 250px; top: 38px; }
  .topping-last { position: absolute; left: 0; width: 100%; top: 250px; font-size: 21px; line-height: 1; }

  .extra-note { position: absolute; left: 44px; top: 808px; width: 172px; text-align: center;
    font-family: "Fredoka", sans-serif; font-weight: 700; font-size: 22px; line-height: 33px; color: var(--gold); }

  .specials { position: absolute; left: 250px; top: 911px; width: 376px; list-style: none;
    text-align: center; font-size: 21px; line-height: 29px; }
</style>
</head>
<body>
<main class="menu">
  <div class="pattern-band" role="img" aria-label="Repeating pattern of cartoon mascot heads on white painted wood"></div>
  <svg class="stage" width="849" height="1200" viewBox="0 0 849 1200" aria-hidden="true">
    <circle cx="424" cy="760" r="720" fill="#f8f7f4"/>
  </svg>

  <div class="photo photo-cup" role="img" aria-label="Iced milk tea in a clear branded cup"></div>
  <div class="photo photo-mango" role="img" aria-label="Ripe mango with a cut slice"></div>
  <div class="photo photo-strawberries" role="img" aria-label="Pile of fresh strawberries"></div>
  <div class="photo photo-raspberries" role="img" aria-label="Fresh raspberries with leaves"></div>
  <div class="mascot-small" role="img" aria-label="Small mascot with heart eyes"></div>

  <h1 class="title title-main">MiLK TEA<span style="font-size:14px">:</span></h1>
  <p class="subline" style="top:160px">Iced of Frapp (blended)&nbsp; -1.6 OMR</p>

  <section class="panel panel-base">
    <h2>CHOOSE YOUR BASE</h2>
    <p>Black Milk Tea</p>
  </section>

  <section class="panel panel-sugar">
    <h2>CHOOSE YOUR SUGAR LEVEL</h2>
    <p>0, 50%, 100%</p>
  </section>

  <section class="panel panel-flavor">
    <h2>CHOOSE YOUR FLAVOR</h2>
    <ul class="list flavor-a"><li>Coconut</li><li>Honeydew</li><li>Mango</li><li>Taro</li><li>Avocado</li></ul>
    <ul class="list flavor-b"><li>Chocolate</li><li>Melon</li><li>Strawberry</li><li>Vanilla</li><li>Pina Colada</li></ul>
  </section>

  <section class="panel panel-toppings">
    <h2>CHOOSE YOUR TOPPINGS</h2>
    <ul class="list topping-a"><li>Tapioca Pearls</li><li>Mango Bubbles</li><li>Lychee Bubbles</li><li>Blueberry Bubbles</li><li>Lemon Bubbles</li><li>Pineapple Jellies</li><li>Mango Jellies</li></ul>
    <ul class="list topping-b"><li>Kiwi Bubbles</li><li>Strawberry Bubbles</li><li>Passion Fruit Bubbles</li><li>Peach Bubbles</li><li>Watermelon Bubbles</li><li>Mixed Coconut Jellies</li><li>Strawberry Jellies</li></ul>
    <p class="topping-last">Coffee Jellies</p>
  </section>

  <p class="extra-note">*EXTRA<br>TAPiOCA OR<br>BUBBLES<br>+300 BZ</p>

  <h2 class="title title-specials">MiLK TEA SPECiALS</h2>
  <p class="subline" style="top:912px;left:0">1.8 OMR</p>
  <ul class="specials" style="top:940px">
    <li>Strawberry Melon Milk Tea</li>
    <li>Taro Strawberry Milk Tea</li>
    <li>Coconut Vanilla Milk Tea</li>
    <li>Taro Coconut Milk Tea</li>
    <li>Pina Colada Milk Tea</li>
    <li>Chocolate Vanilla Milk Tea</li>
  </ul>

  <div class="band-bottom"></div>
</main>
</body>
</html>
```